Website Redesign

We're looking for an artist with experience designing children's websites to redesign a children's video sharing website (like ClipNarvo, but for kids ages 4-14). It should be simple, uncluttered, and easy to use. To see our logo and current layout, go to www.Pebblopa.com. We've uploaded 2 possible layouts that include all elements except the RULES button, but we aren't artists and these might not be the most user-friendly layouts for kids. We've also listed links to some other video-sharing & kids' websites in the target customer section below.
Updates
Thank you for submitting your designs for our website project. We're reviewing all the designs now, and we may contact you to request a slight modification for the home page or for back pages.
Target Market(s)
Kids ages 4-14 who go online to upload & watch videos & images, play games, enter contests, and network. Here are links to some other video-sharing or childrens' websites:
http://wemlorafun.com
http://pavo.com
http://harborotter.com
http://clipnarvo.com
http://tlvjunior.org/
http://marlowe.go.com/index
http://kids.meridianatlasworld.com/kids/
http://www.hiddenmasonry.com
http://www.tots578.com/home.php
Industry/Entity Type
Artists
Requirements
Must have
- Kid-friendly design (easy to use, friendly feel).
Visually simple.
Must include these elements:
-Logo
-Search Bar
-Video Announcement player (see current site, but can be smaller)
-Text Announcement area (can be scrolling)
-Video Categories
-3 Ads (Banner or Video)
-Recent Tags
-Thumbnails of Featured Videos
-Buttons: LOG IN, SIGN UP, UPLOAD, PARENTS, CONTESTS, VIDEOS, IMAGES, GAMES, BLOGS, STORE, RULES.
Nice to have
- We like the rounded look of the buttons on our current site, but let us know if you have another idea.
Should not have
- The design should be for children, but NOT childish because the members range in age from 4-14. The design should have little or no illustrations to clutter the page because we don't want to distract from the content.

```html
<!DOCTYPE html>
<html lang="en">
<head>
<meta charset="utf-8">
<title>Pebblopa – Home</title>
<link href="https://fonts.googleapis.com/css2?family=Arimo:wght@400;700&display=swap" rel="stylesheet">
<style>
:root{
  --yellow:#f7b400;
  --yellow-light:#ffd23c;
  --orange:#f39100;
  --orange-dark:#e07a00;
  --ink:#333333;
  --ink-soft:#6b6b6b;
  --dark:#3b3b3b;
  --page:#e8e8e8;
  --panel:#f3f3f3;
  --line:#d6d6d6;
  --white:#ffffff;
  --footer:#dcdcdc;
}
*{box-sizing:border-box;margin:0;padding:0}
html,body{width:702px;height:1200px;overflow:hidden}
body{font-family:"Arimo",Arial,sans-serif;color:var(--ink);background:var(--page);position:relative;font-size:7px}

/* header */
.masthead{position:absolute;left:0;top:0;width:702px;height:96px;background:linear-gradient(var(--yellow-light),var(--yellow))}
.brand{position:absolute;left:98px;top:30px;width:106px;display:flex;align-items:center;gap:5px;font-weight:700;font-size:17px;line-height:20px;color:var(--dark);white-space:nowrap}
.brand-dot{width:11px;height:11px;flex:none;background:var(--white);border-radius:50%}
.account{position:absolute;right:98px;top:8px;display:flex;gap:4px}
.account span{padding:3px 7px;border-radius:3px;font-weight:700;font-size:6px}
.account .create{background:var(--white);color:var(--ink)}
.account .login{background:var(--orange);color:var(--white)}
.search{position:absolute;left:210px;top:30px;width:394px;height:24px;background:var(--dark);border-radius:4px;display:flex;align-items:center;padding:3px;gap:4px}
.search-icon{width:18px;height:18px;display:flex;align-items:center;justify-content:center}
.search-field{flex:1;height:18px;background:var(--white);border-radius:2px;color:#999;padding:5px 6px;font-size:7px}
.search-cat{width:100px;height:18px;background:var(--white);border-radius:2px;color:#777;padding:5px 6px;font-size:7px}
.search-btn{width:54px;height:18px;background:var(--orange);border-radius:2px;color:var(--white);font-weight:700;text-align:center;line-height:18px;font-size:7px}

.mainnav{position:absolute;left:98px;top:78px;width:506px;height:20px;background:var(--white);border-radius:4px 4px 0 0;display:flex;align-items:center;justify-content:space-between;padding:0 10px;font-weight:700;font-size:6.5px;color:var(--ink-soft)}
.mainnav span{padding:3px 6px;border-right:1px solid var(--line)}
.mainnav .submit{background:var(--dark);color:var(--white);border-radius:2px;border:none}

/* container */
.content{position:absolute;left:98px;top:98px;width:506px;height:944px;background:var(--white)}
.main-col{position:absolute;left:10px;top:14px;width:324px}
.side-col{position:absolute;left:344px;top:14px;width:154px}

.player{height:204px;border:1px solid var(--line)}
.player-title{height:18px;background:var(--dark);color:var(--white);font-weight:700;font-size:7px;padding:5px 8px}
.player-screen{height:160px;background:radial-gradient(ellipse at center,#f0c24a 0%,#a8721a 45%,#3a2608 100%)}
.player-controls{height:24px;background:#222;display:flex;align-items:center;gap:8px;padding:0 6px}
.play-btn{width:22px;height:16px;background:var(--orange);border-radius:2px;display:flex;align-items:center;justify-content:center}
.progress{flex:1;height:4px;background:#555;border-radius:2px;position:relative}
.progress::before{content:"";position:absolute;left:0;top:0;width:58%;height:4px;background:var(--orange);border-radius:2px}

.section-head{margin-top:18px;height:22px;display:flex;justify-content:space-between;align-items:flex-end;border-bottom:1px solid var(--line);padding-bottom:4px}
.section-head h2{font-size:12px;font-weight:700;color:var(--ink);text-transform:uppercase;letter-spacing:-.2px}
.section-head h2 em{font-style:normal;color:var(--orange)}
.view-toggle{display:flex;gap:2px}
.view-toggle i{width:9px;height:9px;background:#bbb;display:block}
.view-toggle i:first-child{background:var(--dark)}

.video-grid{margin-top:8px;display:grid;grid-template-columns:repeat(3,98px);justify-content:space-between;row-gap:12px}
.card{height:140px;border:1px solid var(--line);background:var(--white);padding:4px}
.card-thumb{height:60px;border-radius:2px;position:relative;display:flex;align-items:center;justify-content:center}
.t1{background:linear-gradient(135deg,#c99b6d,#6d4a34)}
.t2{background:linear-gradient(135deg,#d8b08a,#8a5c3f)}
.t3{background:linear-gradient(135deg,#9aa6b0,#4e5861)}
.t4{background:linear-gradient(135deg,#b4553b,#5e2418)}
.play-dot{width:18px;height:18px;background:rgba(255,255,255,.85);border-radius:50%;display:flex;align-items:center;justify-content:center}
.card h3{font-size:7px;font-weight:700;margin-top:5px}
.stars{display:flex;gap:1px;margin-top:3px}
.card p{font-size:5.5px;color:var(--ink-soft);line-height:8px;margin-top:3px}
.read-more{display:block;width:40px;margin:6px auto 0;background:var(--panel);border:1px solid var(--line);border-radius:2px;text-align:center;font-size:5.5px;padding:2px 0;color:var(--ink-soft)}

.pager{margin-top:10px;display:flex;justify-content:space-between;height:24px}
.pager span{width:156px;border-radius:3px;font-weight:700;font-size:8px;line-height:24px;text-align:center}
.pager .prev{background:#d5d5d5;color:var(--ink-soft)}
.pager .next{background:var(--orange);color:var(--white)}

/* side panels */
.panel{border:1px solid var(--line);margin-bottom:12px;background:var(--panel)}
.panel-head{height:18px;background:var(--dark);color:var(--white);font-weight:700;font-size:7px;padding:5px 6px;text-transform:uppercase}
.news-item{display:flex;gap:5px;padding:5px;border-bottom:1px solid var(--line);background:var(--white)}
.mini-thumb{width:34px;height:30px;flex:none;border-radius:2px}
.news-item h4{font-size:6.5px;font-weight:700}
.news-item p{font-size:5px;color:var(--ink-soft);line-height:7px;margin-top:2px}
.panel-arrows{height:14px;display:flex;justify-content:center;gap:30px;align-items:center}
.cat-list{display:grid;grid-template-columns:1fr 1fr;padding:6px;gap:2px 6px;background:var(--white)}
.cat-list span{font-size:6px;color:var(--ink-soft);padding:3px 4px;border-bottom:1px solid var(--line);background:var(--panel)}
.ad-box{height:132px;background:#ececec;border:1px solid var(--line);margin:20px 0 40px}
.tag-cloud{display:flex;flex-wrap:wrap;gap:4px;padding:7px;background:var(--white)}
.tag-cloud span{font-size:5.5px;padding:2px 6px;border-radius:6px;background:var(--orange);color:var(--white)}
.tag-cloud span.g{background:#9a9a9a}
.tag-cloud span.d{background:var(--dark)}

/* banner & footer */
.banner{position:absolute;left:176px;top:1052px;width:350px;height:40px;background:var(--white);border:1px solid var(--line)}
.footer{position:absolute;left:0;top:1100px;width:702px;height:80px;background:var(--footer)}
.footer-cols{position:absolute;left:108px;top:10px;width:490px;display:flex;justify-content:space-between}
.footer-cols div{width:110px}
.footer-cols h5{font-size:7px;font-weight:700;margin-bottom:5px}
.footer-cols p{font-size:5.5px;color:var(--ink-soft);line-height:9px}
.bottom-bar{position:absolute;left:0;top:1180px;width:702px;height:20px;background:var(--dark);color:#bbb;font-size:6px}
.bottom-bar .copy{position:absolute;left:108px;top:7px}
.bottom-bar .follow{position:absolute;right:104px;top:4px;display:flex;align-items:center;gap:4px}
.bottom-bar .follow i{width:12px;height:12px;display:block;border-radius:2px;background:#6a8fc7}
.bottom-bar .follow i + i{background:#5fb8e0}
</style>
</head>
<body>

<header class="masthead">
  <div class="brand"><span class="brand-dot"></span>Pebblopa</div>
  <div class="account"><span class="create">Create New Account</span><span class="login">LOGIN</span></div>
  <div class="search">
    <div class="search-icon"><svg width="10" height="10" viewBox="0 0 10 10"><circle cx="4" cy="4" r="3" fill="none" stroke="#fff" stroke-width="1.4"/><line x1="6.2" y1="6.2" x2="9" y2="9" stroke="#fff" stroke-width="1.6"/></svg></div>
    <div class="search-field">Search your videos</div>
    <div class="search-cat">Select your category ▾</div>
    <div class="search-btn">SEARCH</div>
  </div>
</header>

<nav class="mainnav">
  <span>HOME</span><span>CONTESTS</span><span>VIDEOS</span><span>IMAGES</span><span>GAMES</span><span>BLOGS</span><span>STORE</span><span class="submit">SUBMIT A VIDEO</span><span>PARENTS</span>
</nav>

<main class="content">
  <div class="main-col">
    <section class="player">
      <div class="player-title">VIDEO: NAME WILL BE HERE!</div>
      <div class="player-screen" role="img" aria-label="Announcement video frame with the site name on a glowing golden background"></div>
      <div class="player-controls">
        <div class="play-btn"><svg width="7" height="8" viewBox="0 0 7 8"><path d="M0 0L7 4L0 8Z" fill="#fff"/></svg></div>
        <div class="progress"></div>
        <svg width="10" height="8" viewBox="0 0 10 8"><path d="M0 3h2l3-3v8L2 5H0Z" fill="#aaa"/></svg>
      </div>
    </section>

    <div class="section-head"><h2>Featured <em>Videos</em></h2><div class="view-toggle"><i></i><i></i></div></div>
    <div class="video-grid">
      <article class="card"><div class="card-thumb t1" role="img" aria-label="Video still of kids playing"><span class="play-dot"><svg width="6" height="7" viewBox="0 0 6 7"><path d="M0 0L6 3.5L0 7Z" fill="#333"/></svg></span></div><h3>Video Name</h3><div class="stars"><svg width="30" height="5"><g fill="#f39100"><circle cx="2.5" cy="2.5" r="2"/><circle cx="8.5" cy="2.5" r="2"/><circle cx="14.5" cy="2.5" r="2"/></g><g fill="#ccc"><circle cx="20.5" cy="2.5" r="2"/><circle cx="26.5" cy="2.5" r="2"/></g></svg></div><p>Short clip shared by a young member this week.</p><span class="read-more">Read More</span></article>
      <article class="card"><div class="card-thumb t2" role="img" aria-label="Video still of a child smiling"><span class="play-dot"><svg width="6" height="7" viewBox="0 0 6 7"><path d="M0 0L6 3.5L0 7Z" fill="#333"/></svg></span></div><h3>Video Name</h3><div class="stars"><svg width="30" height="5"><g fill="#f39100"><circle cx="2.5" cy="2.5" r="2"/><circle cx="8.5" cy="2.5" r="2"/><circle cx="14.5" cy="2.5" r="2"/><circle cx="20.5" cy="2.5" r="2"/></g><circle cx="26.5" cy="2.5" r="2" fill="#ccc"/></svg></div><p>Short clip shared by a young member this week.</p><span class="read-more">Read More</span></article>
      <article class="card"><div class="card-thumb t3" role="img" aria-label="Video still placeholder"><span class="play-dot"><svg width="6" height="7" viewBox="0 0 6 7"><path d="M0 0L6 3.5L0 7Z" fill="#333"/></svg></span></div><h3>Video Name</h3><div class="stars"><svg width="30" height="5"><g fill="#f39100"><circle cx="2.5" cy="2.5" r="2"/><circle cx="8.5" cy="2.5" r="2"/><circle cx="14.5" cy="2.5" r="2"/></g><g fill="#ccc"><circle cx="20.5" cy="2.5" r="2"/><circle cx="26.5" cy="2.5" r="2"/></g></svg></div><p>Short clip shared by a young member this week.</p><span class="read-more">Read More</span></article>
      <article class="card"><div class="card-thumb t2" role="img" aria-label="Video still of kids outdoors"><span class="play-dot"><svg width="6" height="7" viewBox="0 0 6 7"><path d="M0 0L6 3.5L0 7Z" fill="#333"/></svg></span></div><h3>Video Name</h3><div class="stars"><svg width="30" height="5"><g fill="#f39100"><circle cx="2.5" cy="2.5" r="2"/><circle cx="8.5" cy="2.5" r="2"/><circle cx="14.5" cy="2.5" r="2"/></g><g fill="#ccc"><circle cx="20.5" cy="2.5" r="2"/><circle cx="26.5" cy="2.5" r="2"/></g></svg></div><p>Short clip shared by a young member this week.</p><span class="read-more">Read More</span></article>
      <article class="card"><div class="card-thumb t1" role="img" aria-label="Video still of a family scene"><span class="play-dot"><svg width="6" height="7" viewBox="0 0 6 7"><path d="M0 0L6 3.5L0 7Z" fill="#333"/></svg></span></div><h3>Video Name</h3><div class="stars"><svg width="30" height="5"><g fill="#f39100"><circle cx="2.5" cy="2.5" r="2"/><circle cx="8.5" cy="2.5" r="2"/><circle cx="14.5" cy="2.5" r="2"/></g><g fill="#ccc"><circle cx="20.5" cy="2.5" r="2"/><circle cx="26.5" cy="2.5" r="2"/></g></svg></div><p>Short clip shared by a young member this week.</p><span class="read-more">Read More</span></article>
      <article class="card"><div class="card-thumb t4" role="img" aria-label="Video still on a red stage"><span class="play-dot"><svg width="6" height="7" viewBox="0 0 6 7"><path d="M0 0L6 3.5L0 7Z" fill="#333"/></svg></span></div><h3>Video Name</h3><div class="stars"><svg width="30" height="5"><g fill="#f39100"><circle cx="2.5" cy="2.5" r="2"/><circle cx="8.5" cy="2.5" r="2"/><circle cx="14.5" cy="2.5" r="2"/></g><g fill="#ccc"><circle cx="20.5" cy="2.5" r="2"/><circle cx="26.5" cy="2.5" r="2"/></g></svg></div><p>Short clip shared by a young member this week.</p><span class="read-more">Read More</span></article>
    </div>

    <div class="section-head"><h2>Contest <em>Videos</em></h2></div>
    <div class="video-grid">
      <article class="card"><div class="card-thumb t2" role="img" aria-label="Contest video still"><span class="play-dot"><svg width="6" height="7" viewBox="0 0 6 7"><path d="M0 0L6 3.5L0 7Z" fill="#333"/></svg></span></div><h3>Video Name</h3><div class="stars"><svg width="30" height="5"><g fill="#f39100"><circle cx="2.5" cy="2.5" r="2"/><circle cx="8.5" cy="2.5" r="2"/><circle cx="14.5" cy="2.5" r="2"/></g><g fill="#ccc"><circle cx="20.5" cy="2.5" r="2"/><circle cx="26.5" cy="2.5" r="2"/></g></svg></div><p>Entry for this month's talent contest.</p><span class="read-more">Read More</span></article>
      <article class="card"><div class="card-thumb t1" role="img" aria-label="Contest video still"><span class="play-dot"><svg width="6" height="7" viewBox="0 0 6 7"><path d="M0 0L6 3.5L0 7Z" fill="#333"/></svg></span></div><h3>Video Name</h3><div class="stars"><svg width="30" height="5"><g fill="#f39100"><circle cx="2.5" cy="2.5" r="2"/><circle cx="8.5" cy="2.5" r="2"/><circle cx="14.5" cy="2.5" r="2"/></g><g fill="#ccc"><circle cx="20.5" cy="2.5" r="2"/><circle cx="26.5" cy="2.5" r="2"/></g></svg></div><p>Entry for this month's talent contest.</p><span class="read-more">Read More</span></article>
      <article class="card"><div class="card-thumb t3" role="img" aria-label="Contest video still placeholder"><span class="play-dot"><svg width="6" height="7" viewBox="0 0 6 7"><path d="M0 0L6 3.5L0 7Z" fill="#333"/></svg></span></div><h3>Video Name</h3><div class="stars"><svg width="30" height="5"><g fill="#f39100"><circle cx="2.5" cy="2.5" r="2"/><circle cx="8.5" cy="2.5" r="2"/><circle cx="14.5" cy="2.5" r="2"/></g><g fill="#ccc"><circle cx="20.5" cy="2.5" r="2"/><circle cx="26.5" cy="2.5" r="2"/></g></svg></div><p>Entry for this month's talent contest.</p><span class="read-more">Read More</span></article>
      <article class="card"><div class="card-thumb t1" role="img" aria-label="Contest video still"><span class="play-dot"><svg width="6" height="7" viewBox="0 0 6 7"><path d="M0 0L6 3.5L0 7Z" fill="#333"/></svg></span></div><h3>Video Name</h3><div class="stars"><svg width="30" height="5"><g fill="#f39100"><circle cx="2.5" cy="2.5" r="2"/><circle cx="8.5" cy="2.5" r="2"/><circle cx="14.5" cy="2.5" r="2"/></g><g fill="#ccc"><circle cx="20.5" cy="2.5" r="2"/><circle cx="26.5" cy="2.5" r="2"/></g></svg></div><p>Entry for this month's talent contest.</p><span class="read-more">Read More</span></article>
      <article class="card"><div class="card-thumb t4" role="img" aria-label="Contest video still on a red stage"><span class="play-dot"><svg width="6" height="7" viewBox="0 0 6 7"><path d="M0 0L6 3.5L0 7Z" fill="#333"/></svg></span></div><h3>Video Name</h3><div class="stars"><svg width="30" height="5"><g fill="#f39100"><circle cx="2.5" cy="2.5" r="2"/><circle cx="8.5" cy="2.5" r="2"/><circle cx="14.5" cy="2.5" r="2"/></g><g fill="#ccc"><circle cx="20.5" cy="2.5" r="2"/><circle cx="26.5" cy="2.5" r="2"/></g></svg></div><p>Entry for this month's talent contest.</p><span class="read-more">Read More</span></article>
      <article class="card"><div class="card-thumb t4" role="img" aria-label="Contest video still on a red stage"><span class="play-dot"><svg width="6" height="7" viewBox="0 0 6 7"><path d="M0 0L6 3.5L0 7Z" fill="#333"/></svg></span></div><h3>Video Name</h3><div class="stars"><svg width="30" height="5"><g fill="#f39100"><circle cx="2.5" cy="2.5" r="2"/><circle cx="8.5" cy="2.5" r="2"/><circle cx="14.5" cy="2.5" r="2"/></g><g fill="#ccc"><circle cx="20.5" cy="2.5" r="2"/><circle cx="26.5" cy="2.5" r="2"/></g></svg></div><p>Entry for this month's talent contest.</p><span class="read-more">Read More</span></article>
    </div>

    <div class="pager"><span class="prev">◂ Previous</span><span class="next">Next ▸</span></div>
  </div>

  <aside class="side-col">
    <section class="panel">
      <div class="panel-head">New Stuff</div>
      <div class="news-item"><div class="mini-thumb t1" role="img" aria-label="News photo"></div><div><h4>Lorem Ipsum Dolor Sit Amet</h4><p>New contest opens on Monday for all members.</p></div></div>
      <div class="news-item"><div class="mini-thumb t2" role="img" aria-label="News photo"></div><div><h4>Lorem Ipsum Dolor Sit Amet</h4><p>Fresh games added to the play zone today.</p></div></div>
      <div class="news-item"><div class="mini-thumb t3" role="img" aria-label="News photo"></div><div><h4>Lorem Ipsum Dolor Sit Amet</h4><p>Parents page updated with safety tips.</p></div></div>
      <div class="panel-arrows"><svg width="8" height="5"><path d="M0 0h8L4 5Z" fill="#333"/></svg><svg width="8" height="5"><path d="M0 5h8L4 0Z" fill="#f39100"/></svg></div>
    </section>

    <section class="panel">
      <div class="panel-head">Video Categories</div>
      <div class="cat-list">
        <span>Cartoon Videos</span><span>Cartoon Videos</span>
        <span>Family Videos</span><span>Family Videos</span>
        <span>Games Videos</span><span>Games Videos</span>
        <span>Music Videos</span><span>Music Videos</span>
        <span>Baby Videos</span><span>Baby Videos</span>
        <span>Comedy Videos</span><span>Comedy Videos</span>
      </div>
    </section>

    <section class="panel">
      <div class="panel-head">Related Videos</div>
      <div class="news-item"><div class="mini-thumb t2" role="img" aria-label="Related video still"></div><div><h4>Lorem Ipsum Dolor Sit</h4><p>Fun clip from our members.</p></div></div>
      <div class="news-item"><div class="mini-thumb t1" role="img" aria-label="Related video still"></div><div><h4>Lorem Ipsum Dolor Sit</h4><p>Fun clip from our members.</p></div></div>
      <div class="news-item"><div class="mini-thumb t3" role="img" aria-label="Related video still"></div><div><h4>Lorem Ipsum Dolor Sit</h4><p>Fun clip from our members.</p></div></div>
      <div class="news-item"><div class="mini-thumb t4" role="img" aria-label="Related video still"></div><div><h4>Lorem Ipsum Dolor Sit</h4><p>Fun clip from our members.</p></div></div>
    </section>

    <div class="ad-box" role="img" aria-label="Advertisement space"></div>

    <section class="panel">
      <div class="panel-head">Recent Tags</div>
      <div class="tag-cloud">
        <span>cartoon</span><span class="g">music</span><span class="d">games</span><span>family</span>
        <span class="g">funny</span><span>dance</span><span class="d">pets</span><span class="g">sports</span>
        <span>art</span><span class="d">science</span><span class="g">songs</span><span>magic</span>
      </div>
    </section>
  </aside>
</main>

<div class="banner" role="img" aria-label="Advertisement banner"></div>

<footer class="footer">
  <div class="footer-cols">
    <div><h5>Home</h5><p>About Us<br>Services<br>Blog<br>Contact</p></div>
    <div><h5>Groups</h5><p>Community<br>Friends<br>Clubs<br>Events</p></div>
    <div><h5>Photos</h5><p>Latest Photos<br>Top Rated<br>Albums</p></div>
    <div><h5>Videos Category</h5><p>Cartoon Videos<br>Music Videos<br>Family Videos</p></div>
  </div>
</footer>
<div class="bottom-bar">
  <span class="copy">© 2013 Pebblopa. All rights reserved.</span>
  <span class="follow">Follow us <i></i><i></i></span>
</div>

</body>
</html>
```